Webdesign Metall- und Stahlbau Harkenfeld GmbH
Zielgruppe
Metall- und Stahlbau Harkenfeld GmbH
Zielgruppe: öffentlicher Bereich, Industrie, Gesundheitswesen > deutschlandweit tätig
Aufgabenstellung
keine bewegten Bilder oder Elemente in der Website
klassisches Layout
sehr konservativ

```html
<!DOCTYPE html>
<html lang="de">
<head>
<meta charset="utf-8">
<title>Metall- und Stahlbau Harkenfeld GmbH</title>
<link href="https://fonts.googleapis.com/css2?family=Arimo:wght@400;700&display=swap" rel="stylesheet">
<style>
:root{
  --yellow:#ffcb3d;
  --blue:#0a0ac8;
  --ink:#1c1c1c;
  --soft:#f7f7f7;
  --white:#ffffff;
  --bar:#2b2b2b;
  --hero-a:#7d8fa6;
  --hero-b:#b89a78;
}
*{margin:0;padding:0;box-sizing:border-box}
html,body{width:757px;height:1200px;overflow:hidden}
body{position:relative;font-family:'Arimo',Arial,sans-serif;color:var(--ink);background:var(--white)}
.abs{position:absolute}
.site-header{left:0;top:0;width:757px;height:45px;background:var(--yellow)}
.brand{left:118px;top:7px;display:flex;align-items:center;gap:5px}
.brand-mark{width:31px;height:31px;background:var(--blue)}
.brand-name{color:var(--blue);font-weight:700;font-size:10.5px;line-height:12px}
.brand-name small{display:block;font-size:5px;line-height:7px}
.main-nav{left:294px;top:19px;display:flex;gap:4px;font-size:6.4px;font-weight:700;white-space:nowrap}
.main-nav span.dot{font-weight:400}
.main-nav .active{color:var(--blue);position:relative}
.main-nav .active::after{content:"";position:absolute;left:-3px;right:-3px;top:20px;height:2px;background:var(--blue)}
.hero{left:0;top:45px;width:757px;height:282px;background:linear-gradient(160deg,#b9c4d2 0%,var(--hero-a) 45%,var(--hero-b) 100%)}
.pill{top:263px;height:24px;border-radius:12px;background:rgba(235,235,235,.93);display:flex;align-items:center;gap:8px;padding-left:12px;font-size:6.6px;font-weight:700}
.pill svg{width:12px;height:12px}
.welcome{left:0;top:327px;width:757px;height:143px;background:var(--soft);text-align:center}
.welcome h1{position:absolute;left:0;right:0;top:49px;font-size:16px;color:var(--blue)}
.welcome .sub{position:absolute;left:0;right:0;top:68px;font-size:10.5px}
.welcome .tag{position:absolute;left:0;right:0;top:87px;font-size:7px;letter-spacing:.5px}
.strengths-intro{left:117px;top:519px;font-size:8.4px}
.strengths-title{left:117px;top:531px;font-size:12px;color:var(--blue);font-weight:700}
.strengths-text{left:117px;top:552px;font-size:6.8px}
.expect{left:117px;top:582px;font-size:6.8px;font-weight:700}
.services{left:117px;top:604px;list-style:none;font-size:6.6px;line-height:14.6px}
.services li::before{content:"";display:inline-block;width:2px;height:2px;background:var(--blue);margin:0 4px 1px 0;vertical-align:middle}
.photo-modules{left:268px;top:599px;width:379px;height:100px;border-radius:40px;background:radial-gradient(ellipse at 55% 55%,#a9cbe6 0%,#cfe2f1 45%,rgba(255,255,255,0) 75%)}
.quality{left:0;top:757px;width:757px;height:249px;background:var(--yellow)}
.quality h2{position:absolute;left:0;right:0;top:46px;text-align:center;font-size:12.6px}
.card{top:835px;width:164px;height:119px;background:var(--white);border-radius:3px;box-shadow:0 3px 10px rgba(0,0,0,.12);text-align:center}
.card svg{position:absolute;left:68px;top:27px;width:28px;height:28px}
.card p{position:absolute;left:6px;right:6px;top:65px;font-size:6.7px;line-height:9.8px}
.contact{left:0;top:1045px;width:757px;text-align:center;font-size:6.7px;line-height:9.8px}
.contact h3{font-size:6.7px;margin-bottom:10px}
.contact p{margin-bottom:10px}
.footer-bar{left:0;top:1181px;width:757px;height:19px;background:var(--bar);color:var(--white);font-size:6px;text-align:center;line-height:19px}
</style>
</head>
<body>
<header class="site-header abs">
  <div class="brand abs">
    <div class="brand-mark"></div>
    <div class="brand-name">Metall- und Stahlbau<br>HARKENFELD GMBH<small>Meisterbetrieb der Innung seit 1965</small></div>
  </div>
  <nav class="main-nav abs">
    <span class="active">Home</span><span class="dot">·</span><span>Leistungen</span><span class="dot">·</span><span>Referenzen</span><span class="dot">·</span><span>Stellenangebote</span><span class="dot">·</span><span>aktuelle Meldungen</span><span class="dot">·</span><span>Download</span><span class="dot">·</span><span>Unternehmensvorstellung</span>
  </nav>
</header>

<section class="hero abs" role="img" aria-label="Luftaufnahme einer Industriehalle im Bau mit Stahlträgern und Dachblechen"></section>
<div class="pill abs" style="left:206px;width:87px">
  <svg viewBox="0 0 24 24"><path fill="#0a0ac8" d="M6.6 10.8a15 15 0 0 0 6.6 6.6l2.2-2.2a1 1 0 0 1 1-.25 11 11 0 0 0 3.6.6 1 1 0 0 1 1 1V20a1 1 0 0 1-1 1A17 17 0 0 1 3 4a1 1 0 0 1 1-1h3.5a1 1 0 0 1 1 1 11 11 0 0 0 .6 3.6 1 1 0 0 1-.25 1z"/></svg>037412 5830</div>
<div class="pill abs" style="left:304px;width:147px">
  <svg viewBox="0 0 24 24"><path fill="#0a0ac8" d="M2 5h20v14H2z"/><path d="M2 6l10 7 10-7" fill="none" stroke="#ebebeb" stroke-width="1.6"/></svg>kontakt@harkenfeld-stahlbau.de</div>
<div class="pill abs" style="left:462px;width:87px">
  <svg viewBox="0 0 24 24"><rect x="3" y="8" width="18" height="13" rx="1" fill="#0a0ac8"/><rect x="7" y="3" width="10" height="6" fill="#0a0ac8"/><rect x="8" y="11" width="8" height="2" fill="#ebebeb"/><rect x="8" y="15" width="8" height="3" fill="#ebebeb"/></svg>037412 5831</div>

<section class="welcome abs">
  <h1>Wir begrüßen Sie recht herzlich auf unseren Seiten.</h1>
  <div class="sub">Metall- und Stahlbau Harkenfeld GmbH</div>
  <div class="tag">Firmenverbund Strahlenschutzbau</div>
</section>

<div class="strengths-intro abs">Unsere Stärken sind</div>
<div class="strengths-title abs">Kompetenz, Qualität und Zuverlässigkeit.</div>
<div class="strengths-text abs">Qualifizierte Mitarbeiter und eine moderne Fertigung erfüllen höchste Qualitätsanforderungen.</div>
<div class="expect abs">Sie können von uns erwarten:</div>
<ul class="services abs">
  <li>Beratung, Planung und Konstruktion</li>
  <li>Metall- und Stahlbau</li>
  <li>Blechbearbeitung</li>
  <li>Fertigung und Montage</li>
  <li>Wartung und Instandhaltung</li>
  <li>kundenspezifische Sonderanfertigungen</li>
  <li>Strahlenschutzbau</li>
</ul>
<div class="photo-modules abs" role="img" aria-label="Hellblaue Raumcontainer-Anlage auf einem Hof"></div>

<section class="quality abs"><h2>Qualitätssicherungssystem:</h2></section>
<div class="card abs" style="left:117px">
  <svg viewBox="0 0 28 28" fill="none" stroke="#222" stroke-width="1"><path d="M6 2h12l4 4v20H6z"/><circle cx="14" cy="10" r="3"/><path d="M9 17h10M9 20h10M9 23h10"/></svg>
  <p>Zertifizierung für Tragende Bauteile und Bausätze für Stahltragwerke bis EXC2 nach EN 1090-2</p>
</div>
<div class="card abs" style="left:296px">
  <svg viewBox="0 0 28 28" fill="none" stroke="#222" stroke-width="1"><path d="M4 24l12-12M14 10l4 4"/><path d="M20 4l1 3 3 1-3 1-1 3-1-3-3-1 3-1z"/><path d="M3 26h10"/></svg>
  <p>Schweißzertifikat nach<br>EN 1090-2:2008+A1:2011, Ausführungsklasse EXC2 nach EN 1090-2</p>
</div>
<div class="card abs" style="left:476px">
  <svg viewBox="0 0 28 28" fill="none" stroke="#222" stroke-width="1"><path d="M5 3h14v22H5z"/><path d="M8 8l1 1 2-2M8 13l1 1 2-2M8 18l1 1 2-2M13 8h4M13 13h4"/><circle cx="20" cy="19" r="4"/><path d="M18 22.5l-1 4 3-1.5 3 1.5-1-4"/></svg>
  <p>Zertifizierung zu<br>Qualitätssicherungssystem,<br>DIN EN ISO 3834-3</p>
</div>

<section class="contact abs">
  <h3>Kontakt</h3>
  <p>Metall- und Stahlbau Harkenfeld GmbH<br>Lindenweg 4<br>09477 Talheim</p>
  <p>Tel.: 037412 5830<br>Fax: 037412 5831</p>
  <p>kontakt@harkenfeld-stahlbau.de</p>
</section>

<footer class="footer-bar abs">© Metall- und Stahlbau Harkenfeld GmbH</footer>
</body>
</html>
```